New DermaLoom logo and packaging

We would like a new design for our new product DermaLoom, a high strength vitamin C serum which treats pigmentation. The packaging will reflect a high quality, clinical product with the logo "DermaLoom" on the front, with it's ingredients "Vitamin C, B3, B5, E and ferulic acid" the products are in two sizes 10ml and 30ml.

This is one of many products to come out in the DermaLoom range.

It would be for high end medical clinics selling premium brands, with a strong medical and clinical feel, professional and current or even futuristic in appearance.

Gold, blue, silver, White, cream are all colours that do this (without appearing cheap)

The product is not tested on animals, so would have
- "Not tested on animals".
- "12m" symbol for shelf life,
- "Made in USA"
- and ingredients list

See attached the product and existing box

Target Market(s)

Medical and aesthetic clinics

Font styles to use
Serif
Sans Serif

Colors
33a6d7
cee9f5
ffffff
fbed22
fee18a

Requirements
Must have
• High end premium brand
Nice to have
• like the idea of gold and silver lettering on cream background
Should not have
• Tacky, over complicated design

```html
<!DOCTYPE html>
<html lang="en">
<head>
<meta charset="utf-8">
<title>DermaLoom Vitamin C Serum Packaging</title>
<link rel="stylesheet" href="https://fonts.googleapis.com/css2?family=Montserrat:wght@300;400;500;600&display=swap">
<style>
  :root {
    --stage: #c9cacc;
    --carton: #ffffff;
    --ink-grey: #5f6064;
    --gold-dark: #8a6a12;
    --gold-mid: #c9a233;
    --gold-light: #f1dc8a;
    --gold-text: #c9a53a;
    --amber-glass: #2e1d12;
    --cap-black: #111111;
    --gold-foil: linear-gradient(120deg, var(--gold-dark) 0%, var(--gold-mid) 28%, var(--gold-light) 45%, var(--gold-mid) 60%, #a7801d 78%, var(--gold-light) 92%, var(--gold-dark) 100%);
  }
  * { box-sizing: border-box; margin: 0; padding: 0; }
  html, body { width: 1200px; height: 1050px; overflow: hidden; }
  body {
    background: radial-gradient(ellipse at 50% 40%, #e4e5e7 0%, var(--stage) 100%);
    font-family: "Montserrat", sans-serif;
    position: relative;
  }
  .brand { font-weight: 500; letter-spacing: -0.5px; white-space: nowrap; line-height: 1; }

  .carton { position: absolute; left: 110px; top: 150px; width: 500px; height: 810px; }
  .carton-top {
    position: absolute; left: 180px; top: 0; width: 320px; height: 100px;
    background: var(--gold-foil);
    display: flex; align-items: center; justify-content: center;
  }
  .carton-top .brand { font-size: 30px; color: rgba(90, 66, 10, 0.55); }
  .carton-side {
    position: absolute; left: 0; top: 100px; width: 180px; height: 710px;
    background: linear-gradient(90deg, #e9e9ea, #f6f6f6);
    border-right: 1px solid #d6d6d8;
  }
  .carton-front {
    position: absolute; left: 180px; top: 100px; width: 320px; height: 710px;
    background: var(--carton);
  }
  .ingredients-list {
    position: absolute; top: 70px; left: 0; width: 100%;
    text-align: center; color: var(--ink-grey); font-size: 16px; line-height: 1.3;
  }
  .claim {
    position: absolute; top: 390px; left: 0; width: 100%;
    display: flex; align-items: center; justify-content: center; gap: 10px;
    color: var(--ink-grey); font-size: 13px; line-height: 1.25;
  }
  .gold-band {
    position: absolute; left: 0; width: 100%;
    background: var(--gold-foil);
    display: flex; align-items: center; justify-content: center;
  }
  .side-foot { bottom: 0; height: 100px; }
  .side-foot span { color: rgba(255,255,255,0.85); font-size: 13px; }
  .name-band { top: 70px; height: 110px; }
  .name-band .brand { color: #ffffff; font-size: 44px; }
  .front-ingredients {
    position: absolute; left: 0; width: 100%; bottom: 125px;
    text-align: center; color: var(--ink-grey); font-size: 21px; line-height: 1.2;
  }
  .front-foot { bottom: 0; height: 100px; }
  .volume { color: rgba(255,255,255,0.9); font-size: 19px; }
  sub { font-size: 0.6em; }

  .bottle { position: absolute; left: 780px; top: 320px; width: 260px; height: 640px; }
  .bottle svg { position: absolute; left: 0; top: 0; }
  .bottle-label {
    position: absolute; left: 0; top: 382px; width: 260px; text-align: center;
  }
  .bottle-label .brand { color: var(--gold-text); font-size: 36px; }
  .bottle-label .formula { margin-top: 28px; color: var(--gold-text); font-size: 18px; line-height: 1.25; }
  .bottle-label .volume { margin-top: 24px; color: var(--gold-text); font-size: 17px; }
</style>
</head>
<body>
  <section class="carton">
    <div class="carton-top"><span class="brand">DermaLoom</span></div>

    <div class="carton-side">
      <p class="ingredients-list">Ingredients:<br>Vitamin C, B<sub>3</sub>, B<sub>5</sub>, E<br>and Ferulic Acid</p>
      <div class="claim">
        <svg width="26" height="30" viewBox="0 0 26 30" aria-label="12 month shelf life" role="img">
          <rect x="3" y="6" width="20" height="22" rx="2" fill="#55565a"/>
          <rect x="1" y="2" width="24" height="6" rx="2" fill="#55565a"/>
          <text x="13" y="22" font-size="8" fill="#fff" text-anchor="middle" font-family="Montserrat, sans-serif">12M</text>
        </svg>
        <span>Not Tested<br>On Animals</span>
      </div>
      <div class="gold-band side-foot"><span>Made in USA</span></div>
    </div>

    <div class="carton-front">
      <div class="gold-band name-band"><span class="brand">DermaLoom</span></div>
      <p class="front-ingredients">Vitamin C, B<sub>3</sub>, B<sub>5</sub>, E<br>and Ferulic Acid</p>
      <div class="gold-band front-foot"><span class="volume">℮ 30 ml | 1 fl. oz</span></div>
    </div>
  </section>

  <section class="bottle">
    <svg width="260" height="640" viewBox="0 0 260 640">
      <rect x="92" y="0" width="76" height="140" rx="34" fill="var(--cap-black)"/>
      <rect x="70" y="130" width="120" height="100" rx="8" fill="var(--cap-black)"/>
      <rect x="60" y="222" width="140" height="12" rx="3" fill="#1c1c1c"/>
      <path d="M80 234 H180 V262 C240 278 260 300 260 340 V620 Q260 640 240 640 H20 Q0 640 0 620 V340 C0 300 20 278 80 262 Z" fill="var(--amber-glass)"/>
      <rect x="0" y="345" width="260" height="275" fill="#2a190f"/>
    </svg>
    <div class="bottle-label">
      <div class="brand">DermaLoom</div>
      <p class="formula">Vitamin C, B<sub>3</sub>, B<sub>5</sub>, E<br>and Ferulic Acid</p>
      <p class="volume">℮ 30 ml | 1 fl. oz</p>
    </div>
  </section>
</body>
</html>
```